Brightwave Reach - Business Card

We need a business card for a Social Media Marketing company that specializes in online marketing for small businesses in Canada using common Social Media platforms such as Pictora, Kinloop, Blinkit & Chirpo.

I have uploaded a copy of our logo which I would like utilized in the business card. We would like the business card to be modern yet classy design.

Our website is www.brightwavereach.ca

Industry/Entity Type

Marketing

Contact Information for Business Card

Email: info@brightwavereach.ca
Website: www.brightwavereach.ca
Telephone: 604-392-5108

Colors

Designer to choose colors to be used in the design.

Requirements
Must have
• Social Media icons on reverse
• Please add some designs with color.

```html
<!DOCTYPE html>
<html lang="en">
<head>
<meta charset="utf-8">
<title>Brightwave Reach – Business Card</title>
<link rel="stylesheet" href="https://fonts.googleapis.com/css2?family=Poppins:wght@400;700&display=swap">
<style>
  :root{
    --page:#e9e9e7;
    --charcoal:#45484b;
    --charcoal-deep:#2f3134;
    --graphite:#5d6063;
    --ink:#141414;
    --silver:#b9bcbf;
    --paper:#ffffff;
    --logo-ink:#3b3c3e;
    --text-light:#f2f2f2;
  }
  *{box-sizing:border-box;margin:0;padding:0}
  html,body{width:1200px;height:784px;overflow:hidden;background:var(--page)}
  body{position:relative;font-family:"Poppins",sans-serif}

  .card{position:absolute;width:540px;height:309px;overflow:hidden;
        box-shadow:0 6px 18px rgba(0,0,0,.18)}

  /* reverse side */
  .card--back{left:70px;top:60px;
        background:linear-gradient(135deg,var(--charcoal-deep) 0%,var(--charcoal) 55%,var(--graphite) 100%)}
  .dot-field{position:absolute;inset:0;
        background:radial-gradient(ellipse 70% 90% at 92% 40%,rgba(200,203,206,.55) 0%,rgba(160,163,166,.3) 45%,rgba(90,93,96,0) 80%)}
  .back-brand{position:absolute;left:0;right:0;top:92px;text-align:center;
        color:var(--paper);font-weight:700;font-size:36px;line-height:1.05;letter-spacing:1px;text-transform:uppercase}
  .social-list{position:absolute;left:0;right:0;top:224px;display:flex;justify-content:center;gap:22px;
        list-style:none;color:var(--paper);font-size:12px;font-weight:400}
  .social-list li{display:flex;align-items:center;gap:6px}
  .social-list .mark{width:10px;height:10px;background:var(--paper);border-radius:2px}

  /* front side */
  .card--front{left:590px;top:420px;background:var(--charcoal)}
  .front-shapes{position:absolute;inset:0}
  .network-art{position:absolute;left:360px;top:18px;width:166px;height:130px;
        background:radial-gradient(ellipse at 70% 35%,#8a8d90 0%,#5f6265 55%,rgba(69,72,75,0) 100%)}
  .front-brand{position:absolute;left:24px;top:100px;width:250px;text-align:center;
        color:var(--logo-ink);font-weight:700;font-size:32px;line-height:1.05;letter-spacing:1px;text-transform:uppercase}
  .contact{position:absolute;left:364px;right:14px;top:194px;list-style:none;color:var(--text-light);
        font-size:11px;line-height:23px;white-space:nowrap}
  .contact li{display:flex;align-items:center;gap:8px}
  .contact svg{width:11px;height:11px;flex:none}
</style>
</head>
<body>

<section class="card card--back" aria-label="Card reverse">
  <div class="dot-field" role="img" aria-label="Halftone pattern of grey dots growing toward the right"></div>
  <h1 class="back-brand">Brightwave<br>Reach</h1>
  <ul class="social-list">
    <li><span class="mark"></span>Pictora</li>
    <li><span class="mark"></span>Kinloop</li>
    <li><span class="mark"></span>Chirpo</li>
  </ul>
</section>

<section class="card card--front" aria-label="Card front">
  <svg class="front-shapes" viewBox="0 0 540 309" width="540" height="309" aria-hidden="true">
    <path d="M0 0 H318 C378 80 372 232 300 309 H0 Z" fill="var(--ink)"/>
    <path d="M286 0 C352 84 348 226 276 309" fill="none" stroke="var(--silver)" stroke-width="3"/>
    <path d="M0 0 H272 C338 86 332 226 262 309 H0 Z" fill="var(--paper)"/>
  </svg>
  <div class="network-art" role="img" aria-label="Network of connected people icons with a hand touching a node"></div>
  <h2 class="front-brand">Brightwave<br>Reach</h2>
  <ul class="contact">
    <li>
      <svg viewBox="0 0 12 12"><path d="M2.5 1 L4.5 1 L5.2 3.5 L4 4.5 C4.7 6 6 7.3 7.5 8 L8.5 6.8 L11 7.5 L11 9.5 C11 10.3 10.3 11 9.5 11 C5 11 1 7 1 2.5 C1 1.7 1.7 1 2.5 1 Z" fill="var(--text-light)"/></svg>
      604-392-5108
    </li>
    <li>
      <svg viewBox="0 0 12 12"><rect x="0.5" y="2" width="11" height="8" rx="1" fill="var(--text-light)"/><path d="M1 2.5 L6 6.5 L11 2.5" fill="none" stroke="var(--charcoal)" stroke-width="1"/></svg>
      info@brightwavereach.ca
    </li>
    <li>
      <svg viewBox="0 0 12 12"><g fill="none" stroke="var(--text-light)" stroke-width="1"><circle cx="6" cy="6" r="5"/><ellipse cx="6" cy="6" rx="2.2" ry="5"/><path d="M1 6 H11 M2 3.3 H10 M2 8.7 H10"/></g></svg>
      www.brightwavereach.ca
    </li>
  </ul>
</section>

</body>
</html>
```